Business Card Design Project

I need a business card for an environmentally friendly interior design company called Roomcraft Willow.
I was thinking it might be nice to print the business cards on brown recycled paper with green ink.
In addition to interior design, I will also be able to consult with homeowners regarding their indoor environments and how they might be affecting their health after May 2013 which is when I will complete my certification program. This can be added to the business card at that time: "Certified Habitat Vitalis Dwelling Consultant".
Health

```html
<!DOCTYPE html>
<html lang="en">
<head>
<meta charset="utf-8">
<title>Roomcraft Willow — Business Card</title>
<link href="https://fonts.googleapis.com/css2?family=Questrial&display=swap" rel="stylesheet">
<style>
  :root {
    --bark: #5a3c0a;
    --leaf: #b3c41a;
    --backdrop: #ece8e1;
    --shadow: rgba(40, 28, 10, 0.28);
  }
  * { margin: 0; padding: 0; box-sizing: border-box; }
  html, body {
    width: 1200px;
    height: 900px;
    overflow: hidden;
    background: var(--backdrop);
    font-family: "Questrial", "Century Gothic", sans-serif;
  }
  .canvas {
    position: relative;
    width: 1200px;
    height: 900px;
  }
  .card {
    position: absolute;
    top: 300px;
    width: 520px;
    height: 300px;
    overflow: hidden;
    box-shadow: 0 6px 18px var(--shadow);
  }
  .card--front { left: 50px; background: var(--bark); }
  .card--back  { left: 630px; background: var(--leaf); }

  .card__divider {
    position: absolute;
    top: 0;
    width: 2px;
  }
  .card--front .card__divider { left: 188px; bottom: 22px; background: var(--leaf); }
  .card--back .card__divider  { left: 150px; bottom: 0; background: var(--bark); }

  .card__base-band {
    position: absolute;
    left: 0; right: 0; bottom: 0;
    height: 22px;
    background: var(--leaf);
  }

  .card__title {
    position: absolute;
    font-size: 34px;
    font-weight: 400;
    letter-spacing: 0.2px;
    white-space: nowrap;
  }
  .card--front .card__title { left: 212px; top: 56px; color: var(--leaf); }
  .card--back .card__title  { left: 172px; top: 74px; color: var(--bark); font-size: 36px; }

  .contact {
    position: absolute;
    left: 16px;
    top: 196px;
    color: var(--leaf);
  }
  .contact__name { font-size: 15px; margin-left: 18px; }
  .contact__phone {
    display: flex;
    align-items: center;
    gap: 6px;
    font-size: 13px;
    margin-top: 4px;
  }
  .contact__icon { width: 12px; height: 12px; }

  .services {
    position: absolute;
    left: 206px;
    top: 176px;
    list-style: none;
    color: var(--leaf);
    font-size: 11.5px;
    line-height: 16px;
  }
</style>
</head>
<body>
<main class="canvas">
  <section class="card card--front" aria-label="Card front">
    <div class="card__divider"></div>
    <h1 class="card__title">Roomcraft Willow</h1>
    <div class="contact">
      <p class="contact__name">Nora Beth Lane</p>
      <p class="contact__phone">
        <svg class="contact__icon" viewBox="0 0 12 12" aria-hidden="true">
          <rect x="2.5" y="0.5" width="7" height="11" rx="1.2" fill="none" stroke="#b3c41a" stroke-width="1"/>
          <line x1="4.5" y1="9.5" x2="7.5" y2="9.5" stroke="#b3c41a" stroke-width="1"/>
        </svg>
        (555) 318-0472
      </p>
    </div>
    <ul class="services">
      <li>Roomcraft Willow</li>
      <li>Environmentally friendly design</li>
      <li>Certified Habitat Vitalis Dwelling Consultant</li>
    </ul>
    <div class="card__base-band"></div>
  </section>

  <section class="card card--back" aria-label="Card back">
    <div class="card__divider"></div>
    <h2 class="card__title">Roomcraft Willow</h2>
  </section>
</main>
</body>
</html>
```